Modern, sales-driven landing page with video for a photovoltaic configurator

Please create a modern landing page for a photovoltaic configurator where users can select a photovoltaic system, including installation, without entering any personal data. Users can assemble a complete package from our product portfolio and receive a realistic yield and profitability calculation, as well as a complete offer including installation. The landing page should be promoted under the Glanzhof brand (Your Glanzhof Photovoltaic Configurator...). The landing page will be hosted on its own domain: www.glanzhof-energie.de. When submitting an inquiry, users will be redirected to our main website: www.wendel-lichtwerk.de. Text and design suggestions are attached. It is important that both the Glanzhof and Wendel LichtWerk logos are included. Logos are also attached. Various certificates and seals are also included.
Sternwert star ratings and 2-3 customer reviews should be visible. The image should show a tablet with a configurator. Preview images of the configurator and the results (offer, profitability calculation) should be included.

Target Market(s)

homeowners

Coding

Coded - Design and coding required

Font styles to use
Other font styles liked:
• Poppins Bold, Inter

Requirements
Nice to have
• The page should be dark and modern.

```html
<!DOCTYPE html>
<html lang="de">
<head>
<meta charset="utf-8">
<title>Glanzhof Photovoltaik-Konfigurator</title>
<link href="https://fonts.googleapis.com/css2?family=Poppins:wght@500;600;700&family=Inter:wght@400;500;600&display=swap" rel="stylesheet">
<style>
:root{
  --bg:#050a18;
  --bg-2:#081024;
  --card:#0b1429;
  --card-2:#0e1931;
  --line:#1a2540;
  --orange:#ff9800;
  --orange-2:#ffae1a;
  --text:#ffffff;
  --muted:#9aa3b8;
  --pill-bg:#1a140c;
  --pill-line:#6b4a1a;
  --red:#e8413a;
  --green:#2fbf5a;
}
*{box-sizing:border-box;margin:0;padding:0}
html,body{width:1200px;height:5240px;overflow:hidden}
body{background:var(--bg);color:var(--text);font-family:"Inter",sans-serif;font-size:12px;position:relative}
h1,h2,h3,.display{font-family:"Poppins",sans-serif;font-weight:700}
.section{position:absolute;left:0;width:1200px}
.center{text-align:center}
.pill{display:inline-block;padding:9px 22px;border:1px solid var(--pill-line);background:var(--pill-bg);border-radius:20px;font-size:11.5px;color:#e6e6e6}
.btn{display:inline-block;background:var(--orange);color:#fff;font-family:"Poppins",sans-serif;font-weight:600;font-size:12px;padding:12px 30px;border-radius:22px}
.h2{font-size:29px;margin-top:14px;letter-spacing:-.2px}
.sub{color:var(--muted);font-size:11px;margin-top:10px;line-height:1.55}
.icon-badge{width:62px;height:62px;border-radius:50%;background:var(--orange);display:flex;align-items:center;justify-content:center;margin:0 auto;box-shadow:0 0 0 6px rgba(255,152,0,.15)}
.icon-badge svg{width:30px;height:30px;stroke:#fff;fill:none;stroke-width:1.8;stroke-linecap:round;stroke-linejoin:round}
.check{display:inline-flex;width:12px;height:12px;border-radius:50%;background:var(--orange);align-items:center;justify-content:center;flex:none}
.check svg{width:8px;height:8px;stroke:#fff;fill:none;stroke-width:2.4}

/* header + hero */
.hero{top:0;height:653px}
.hero-bg{position:absolute;inset:0;background:
  linear-gradient(180deg,rgba(5,10,24,.9) 0%,rgba(12,24,48,.75) 35%,rgba(24,44,80,.7) 55%,rgba(10,20,44,.85) 100%),
  linear-gradient(180deg,#0b1730 0%,#1d3156 55%,#13254a 75%,#0a1430 100%)}
.hero-bg::after{content:"";position:absolute;left:0;right:0;top:420px;bottom:0;background:repeating-linear-gradient(90deg,rgba(120,150,200,.08) 0 2px,transparent 2px 60px)}
.header{position:absolute;top:0;left:0;width:1200px;height:76px;display:flex;align-items:center;justify-content:space-between;padding:0 114px 0 94px;z-index:2}
.brand{display:flex;align-items:center;gap:12px;font-family:"Poppins",sans-serif;font-weight:600;font-size:19px;letter-spacing:.5px;color:#fff}
.brand .dot{width:58px;height:58px;border-radius:50%;background:var(--orange)}
.header .btn{padding:12px 26px;font-size:11.5px}
.hero-content{position:absolute;top:155px;left:0;width:1200px;text-align:center;z-index:2}
.hero h1{font-size:36px;margin-top:22px;letter-spacing:-.3px}
.hero .lead{font-family:"Poppins",sans-serif;font-weight:600;font-size:12px;margin-top:14px}
.hero .intro{font-size:10.5px;color:#d7dbe4;margin-top:12px;line-height:1.5}
.hero-checks{display:flex;justify-content:center;gap:56px;margin-top:22px;font-size:10.5px;color:#e6e8ee}
.hero-checks span{display:flex;align-items:center;gap:8px}
.hero .btn{margin-top:22px;padding:13px 28px}

/* stats */
.stats{top:653px;height:92px;background:var(--orange);display:flex;padding:0 100px}
.stat{flex:1;text-align:center;display:flex;flex-direction:column;justify-content:center;border-right:1px solid rgba(255,255,255,.35);margin:12px 0}
.stat:last-child{border-right:none}
.stat b{font-family:"Poppins",sans-serif;font-size:30px;line-height:1}
.stat span{font-size:10.5px;margin-top:6px}

/* steps */
.steps{top:745px;height:545px;padding-top:92px}
.card-row{display:grid;grid-template-columns:repeat(3,274px);gap:21px;justify-content:center;margin-top:34px}
.step-card{background:var(--card);border-radius:8px;height:181px;padding:22px 26px 0;text-align:center}
.step-card h3{font-size:13px;margin-top:16px}
.step-card p{font-size:10px;color:var(--muted);line-height:1.55;margin-top:8px}
.steps .btn{margin-top:36px}

/* why */
.why{top:1290px;height:540px}
.why-left{position:absolute;left:110px;top:44px;width:430px}
.why-left .h2{font-size:29px;line-height:1.2;margin-top:18px}
.why-left .text{font-size:10.5px;color:#cfd4df;line-height:1.55;margin-top:16px}
.why-list{margin-top:14px}
.why-list li{list-style:none;display:flex;align-items:center;gap:12px;height:34px;padding-left:14px;margin-bottom:10px;background:linear-gradient(90deg,#0b1429,rgba(11,20,41,.2));border-radius:4px;font-size:10.5px}
.why-left .btn{margin-top:22px}
.cmp{position:absolute;background:var(--card);border-radius:8px;padding:22px 22px}
.cmp h4{font-family:"Poppins",sans-serif;font-weight:600;font-size:11.5px;margin-bottom:16px}
.cmp li{list-style:none;display:flex;align-items:center;gap:10px;font-size:10px;height:31px}
.mark{width:14px;height:14px;border-radius:50%;flex:none;display:flex;align-items:center;justify-content:center}
.mark svg{width:8px;height:8px;stroke-width:2.4;fill:none}
.mark.no{border:1.5px solid var(--red)}.mark.no svg{stroke:var(--red)}
.mark.yes{background:var(--green)}.mark.yes svg{stroke:#fff}
.cmp-others{left:620px;top:92px;width:224px;height:205px}
.cmp-us{left:864px;top:185px;width:220px;height:203px}

/* advantages */
.adv{top:1830px;height:640px;padding-top:58px}
.adv-grid{display:grid;grid-template-columns:repeat(3,274px);grid-auto-rows:183px;gap:20px 21px;justify-content:center;margin-top:30px}
.adv-card{background:var(--card);border-radius:8px;padding:20px 24px 0;text-align:center}
.adv-card h3{font-size:13px;margin-top:14px}
.adv-card p{font-size:10px;color:var(--muted);line-height:1.55;margin-top:7px}

/* audience */
.aud{top:2470px;height:590px;padding-top:64px}
.aud-grid{position:absolute;left:96px;top:211px;display:grid;grid-template-columns:281px 281px;grid-auto-rows:131px;gap:16px 12px}
.aud-card{background:var(--card);border-radius:8px;padding:18px 16px}
.aud-card .top{display:flex;align-items:center;gap:16px}
.aud-card .icon-badge{width:50px;height:50px;margin:0;box-shadow:none}
.aud-card .icon-badge svg{width:24px;height:24px}
.aud-card h3{font-size:13.5px}
.aud-card p{font-size:10px;color:var(--muted);line-height:1.55;margin-top:14px}
.aud-image{position:absolute;left:702px;top:245px;width:404px;height:285px;border-radius:10px;background:linear-gradient(135deg,#0c1530 0%,#1b3a8c 40%,#2c4fb0 60%,#0c1530 100%);opacity:.95}
.aud .btn{position:absolute;left:94px;top:520px}

/* modules */
.mod{top:3060px;height:580px;padding-top:50px}
.tabs{display:inline-flex;gap:8px;margin-top:22px}
.tab{padding:12px 28px;border-radius:22px;background:#172038;font-family:"Poppins",sans-serif;font-weight:600;font-size:11.5px}
.tab.active{background:var(--orange)}
.mod-grid{display:grid;grid-template-columns:268px 264px 264px;gap:31px;justify-content:center;margin-top:24px;text-align:left}
.mod-card{background:var(--card);border-radius:8px;height:153px;padding:12px 16px}
.tag{display:inline-block;font-size:9px;padding:4px 14px;border-radius:12px;background:#2a1d0c;color:#f0c07a;border:1px solid #5a3c12}
.mod-card h3{font-size:13px;margin-top:14px}
.mod-card .desc{font-size:9.5px;color:var(--muted);margin-top:6px}
.specs{display:flex;justify-content:space-around;margin-top:20px;background:var(--card-2);border-radius:6px;padding:10px 0}
.specs div{text-align:center}
.specs b{display:block;color:var(--orange);font-family:"Poppins",sans-serif;font-size:13px}
.specs span{font-size:9px;color:var(--muted)}
.mod .btn{margin-top:26px}

/* calc */
.calc{top:3640px;height:560px}
.calc-card{position:absolute;left:126px;top:72px;width:407px;height:408px;background:var(--card);border-radius:8px;padding:24px 22px}
.calc-card .title{font-family:"Poppins",sans-serif;font-weight:600;font-size:11px}
.price{display:flex;align-items:baseline;gap:8px;margin-top:12px}
.price small{font-size:10px;color:var(--muted)}
.price b{font-family:"Poppins",sans-serif;font-size:34px;color:var(--orange)}
.calc-card .note{font-size:10.5px;color:#d7dbe4;margin-top:10px}
.calc-rows{margin-top:14px}
.calc-rows div{display:flex;justify-content:space-between;font-size:10.5px;height:34px;align-items:center;border-bottom:1px solid var(--line);color:#d0d5e0}
.calc-rows div b{color:#fff;font-weight:600}
.calc-card .btn{display:block;width:196px;margin:18px auto 0;text-align:center;padding:13px 0}
.calc-right{position:absolute;left:603px;top:113px;width:480px}
.calc-right h2{font-size:28px;margin-top:20px}
.calc-right .text{font-size:10.5px;color:#cfd4df;line-height:1.55;margin-top:14px}
.calc-list{margin-top:22px}
.calc-list li{list-style:none;display:flex;align-items:center;gap:12px;font-size:10.5px;height:44px}
.calc-right .btn{margin-top:20px}

/* reviews */
.rev{top:4200px;height:420px;padding-top:62px}
.rev-grid{display:grid;grid-template-columns:repeat(3,274px);gap:21px;justify-content:center;margin-top:22px;text-align:left}
.rev-card{background:var(--card);border-radius:8px;height:173px;padding:20px 20px}
.stars{color:var(--orange);font-size:13px;letter-spacing:1px}
.rev-card p{font-style:italic;font-size:10px;line-height:1.55;margin-top:10px;color:#e8eaf0}
.who{display:flex;align-items:center;gap:12px;margin-top:16px;font-family:"Poppins",sans-serif;font-weight:600;font-size:10.5px}
.avatar{width:30px;height:30px;border-radius:50%;background:#1f6fd6;display:flex;align-items:center;justify-content:center;font-size:10px}

/* cta */
.cta{top:4620px;height:320px;padding-top:22px}
.cta h2{font-size:29px;line-height:1.2;margin-top:16px}
.cta .accent{color:var(--orange);font-family:"Poppins",sans-serif;font-weight:600;font-size:12px;margin-top:12px}
.cta .btn{margin-top:22px}

/* footer */
.footer{top:4940px;height:300px;border-top:1px solid #111a30}
.f-brand{position:absolute;left:114px;top:56px;width:230px}
.f-brand .brand{font-size:14px;gap:8px;color:var(--orange)}
.f-brand .brand .dot{width:20px;height:20px}
.f-brand p{font-size:10.5px;color:var(--muted);line-height:1.55;margin-top:12px}
.powered{display:flex;align-items:center;gap:8px;font-size:9.5px;color:var(--muted);margin-top:10px}
.powered i{width:12px;height:12px;border-radius:50%;background:#ffc400;display:block}
.f-col{position:absolute;top:58px}
.f-col h5{font-family:"Poppins",sans-serif;font-size:9.5px;letter-spacing:1.2px;color:#55607a;font-weight:600}
.f-col li{list-style:none;font-size:11px;color:var(--muted);margin-top:14px}
.f-bottom{position:absolute;left:114px;right:114px;top:252px;padding-top:12px;border-top:1px solid #111a30;display:flex;justify-content:space-between;font-size:9.5px;color:#6b7590}
.f-bottom b{color:#c9ced9;font-weight:500}
</style>
</head>
<body>

<!-- HERO -->
<section class="section hero">
  <div class="hero-bg" role="img" aria-label="Weites Solarfeld unter dunklem Abendhimmel"></div>
  <header class="header">
    <div class="brand"><span class="dot"></span>GLANZHOF</div>
    <a class="btn">Konfigurator starten</a>
  </header>
  <div class="hero-content">
    <span class="pill">GLANZHOF Photovoltaik-Konfigurator</span>
    <h1>Ihre Photovoltaikanlage Ehrlich Kalkuliert.</h1>
    <p class="lead">Mit dem GLANZHOF Photovoltaik-Konfigurator.</p>
    <p class="intro">Konfigurieren Sie Ihre Solaranlage in wenigen Schritten – für Einfamilienhaus, Gewerbehalle oder alles dazwischen.<br>Direkt. Transparent. Unverbindlich.</p>
    <div class="hero-checks">
      <span><i class="check"><svg viewBox="0 0 10 10"><path d="M2 5.2l2 2 4-4.4"/></svg></i>Ergebnis ohne Angabe persönlicher Daten.</span>
      <span><i class="check"><svg viewBox="0 0 10 10"><path d="M2 5.2l2 2 4-4.4"/></svg></i>Für private &amp; gewerbliche Dächer jeder Größe.</span>
      <span><i class="check"><svg viewBox="0 0 10 10"><path d="M2 5.2l2 2 4-4.4"/></svg></i>Realistische Einschätzung statt Lockpreise.</span>
    </div>
    <a class="btn">Jetzt PV-Anlage konfigurieren</a>
  </div>
</section>

<!-- STATS -->
<section class="section stats">
  <div class="stat"><b>1.000+</b><span>Zufriedene Kunden</span></div>
  <div class="stat"><b>4,8</b><span>Sternwert Bewertung</span></div>
  <div class="stat"><b>70%</b><span>Stromkosten sparen</span></div>
  <div class="stat"><b>2 Min.</b><span>Zum Ergebnis</span></div>
  <div class="stat"><b>0€</b><span>Kostenlos &amp; anonym</span></div>
</section>

<!-- STEPS -->
<section class="section steps center">
  <span class="pill">So einfach geht's</span>
  <h2 class="h2">Was kann der Solar-Konfigurator?</h2>
  <p class="sub">Sie legen die Eckdaten fest – wir liefern eine nachvollziehbare Auswertung zu Anlagengröße, Komponenten<br>und realistischer Wirtschaftlichkeit.</p>
  <div class="card-row">
    <div class="step-card">
      <div class="icon-badge"><svg viewBox="0 0 24 24"><path d="M12 21s-6-6-6-11a6 6 0 0 1 12 0c0 5-6 11-6 11z"/><circle cx="12" cy="10" r="2.2"/></svg></div>
      <h3>Adresse &amp; Dach eingeben</h3>
      <p>Geben Sie die Lage Ihres Dachs an. Wir ermitteln die optimale Ausrichtung und Sonnenstunden für Ihren Standort.</p>
    </div>
    <div class="step-card">
      <div class="icon-badge"><svg viewBox="0 0 24 24"><circle cx="12" cy="12" r="3"/><path d="M12 3v3M12 18v3M3 12h3M18 12h3M5.6 5.6l2.1 2.1M16.3 16.3l2.1 2.1M5.6 18.4l2.1-2.1M16.3 7.7l2.1-2.1"/></svg></div>
      <h3>Komponenten auswählen</h3>
      <p>Wählen Sie Solarmodule, Wechselrichter und optional einen Energiespeicher aus unserem Produktportfolio.</p>
    </div>
    <div class="step-card">
      <div class="icon-badge"><svg viewBox="0 0 24 24"><path d="M6 3h9l3 3v15H6z"/><path d="M9 12l2 2 4-4"/></svg></div>
      <h3>Ergebnis sofort erhalten</h3>
      <p>Sie erhalten sofort einen realistischen Angebotspreis, eine Ertrags- und Wirtschaftlichkeitsanalyse komplett kostenlos.</p>
    </div>
  </div>
  <a class="btn">Jetzt persönliche PV-Auswertung erhalten</a>
</section>

<!-- WHY -->
<section class="section why">
  <div class="why-left">
    <span class="pill">Warum Glanzhof Anders ist</span>
    <h2 class="h2">Warum unser<br>Konfigurator anders ist</h2>
    <p class="text">Viele Solarrechner zeigen Ergebnisse erst nach Eingabe Ihrer Kontaktdaten. Wir zeigen Ihr Ergebnis zuerst. Wir gehen bewusst einen anderen Weg.</p>
    <ul class="why-list">
      <li><i class="check"><svg viewBox="0 0 10 10"><path d="M2 5.2l2 2 4-4.4"/></svg></i>Keine Datensammlung – Ihre Daten bleiben bei Ihnen.</li>
      <li><i class="check"><svg viewBox="0 0 10 10"><path d="M2 5.2l2 2 4-4.4"/></svg></i>Kein Verkaufsdruck – Sie entscheiden, wann Sie Kontakt aufnehmen.</li>
      <li><i class="check"><svg viewBox="0 0 10 10"><path d="M2 5.2l2 2 4-4.4"/></svg></i>Keine Lockpreise – realistische Einschätzung statt künstlich niedriger Preise</li>
      <li><i class="check"><svg viewBox="0 0 10 10"><path d="M2 5.2l2 2 4-4.4"/></svg></i>Ergebnis auch ohne Kontaktaufnahme nutzbar</li>
    </ul>
    <a class="btn">Ergebnis ohne Daten sehen</a>
  </div>
  <div class="cmp cmp-others">
    <h4>Andere Anbieter</h4>
    <ul>
      <li><i class="mark no"><svg viewBox="0 0 10 10"><path d="M3 3l4 4M7 3l-4 4"/></svg></i>Ergebnis nur mit Dateneingabe</li>
      <li><i class="mark no"><svg viewBox="0 0 10 10"><path d="M3 3l4 4M7 3l-4 4"/></svg></i>Sofortiger Rückruf</li>
      <li><i class="mark no"><svg viewBox="0 0 10 10"><path d="M3 3l4 4M7 3l-4 4"/></svg></i>Künstlich niedrige Preise</li>
      <li><i class="mark no"><svg viewBox="0 0 10 10"><path d="M3 3l4 4M7 3l-4 4"/></svg></i>Verkaufsdruck</li>
      <li><i class="mark no"><svg viewBox="0 0 10 10"><path d="M3 3l4 4M7 3l-4 4"/></svg></i>Daten an Dritte</li>
    </ul>
  </div>
  <div class="cmp cmp-us">
    <h4>Glanzhof</h4>
    <ul>
      <li><i class="mark yes"><svg viewBox="0 0 10 10"><path d="M2 5.2l2 2 4-4.4"/></svg></i>Ergebnis sofort &amp; anonym</li>
      <li><i class="mark yes"><svg viewBox="0 0 10 10"><path d="M2 5.2l2 2 4-4.4"/></svg></i>Kein Telefonterror</li>
      <li><i class="mark yes"><svg viewBox="0 0 10 10"><path d="M2 5.2l2 2 4-4.4"/></svg></i>Realistische Preise</li>
      <li><i class="mark yes"><svg viewBox="0 0 10 10"><path d="M2 5.2l2 2 4-4.4"/></svg></i>Sie entscheiden</li>
      <li><i class="mark yes"><svg viewBox="0 0 10 10"><path d="M2 5.2l2 2 4-4.4"/></svg></i>Keine Datenweitergabe</li>
    </ul>
  </div>
</section>

<!-- ADVANTAGES -->
<section class="section adv center">
  <span class="pill">Ihre Vorteile</span>
  <h2 class="h2">In wenigen Minuten zu Ihrem Preis</h2>
  <p class="sub">Erhalten Sie sofort – einfach, unverbindlich, anonym und komplett kostenlos.</p>
  <div class="adv-grid">
    <div class="adv-card">
      <div class="icon-badge"><svg viewBox="0 0 24 24"><path d="M6 3h12v18H6z"/><path d="M9 8h6M9 12h6M9 16h3"/></svg></div>
      <h3>Realistischer Angebotspreis</h3>
      <p>Kein Lockpreis, keine versteckten Kosten. Sie sehen einen ehrlichen, kalkulierten Festpreis inklusive Montage direkt.</p>
    </div>
    <div class="adv-card">
      <div class="icon-badge"><svg viewBox="0 0 24 24"><path d="M4 20V10M10 20V5M16 20v-8M22 20H2"/></svg></div>
      <h3>Wirtschaftlichkeitsanalyse</h3>
      <p>Wie viel Strom erzeugt Ihre Anlage? Wann amortisiert sie sich? Konkrete Zahlen statt Verkaufsversprechen.</p>
    </div>
    <div class="adv-card">
      <div class="icon-badge"><svg viewBox="0 0 24 24"><path d="M3 18l3-12h12l3 12z"/><path d="M7.5 6L6 18M12 6v12M16.5 6L18 18M4.5 12h15"/></svg></div>
      <h3>Schlüsselfertiges Solarkonzept</h3>
      <p>Ein modernes, vollständiges Solarpaket inkl. Installation – Sie können alles bequem aus unserer Produktpalette.</p>
    </div>
    <div class="adv-card">
      <div class="icon-badge"><svg viewBox="0 0 24 24"><path d="M12 3l7 3v6c0 4.5-3 7.5-7 9-4-1.5-7-4.5-7-9V6z"/><path d="M9 12l2 2 4-4"/></svg></div>
      <h3>datenschutzkonform</h3>
      <p>Keine Registrierung, keine E-Mail, kein Telefon erforderlich. Ihre Daten bleiben bei Ihnen.</p>
    </div>
    <div class="adv-card">
      <div class="icon-badge"><svg viewBox="0 0 24 24"><circle cx="12" cy="12" r="3"/><path d="M12 3v3M12 18v3M3 12h3M18 12h3M5.6 5.6l2.1 2.1M16.3 16.3l2.1 2.1M5.6 18.4l2.1-2.1M16.3 7.7l2.1-2.1"/></svg></div>
      <h3>Freie Komponentenwahl</h3>
      <p>Solarmodule, Wechselrichter, Energiespeicher – Sie wählen selbst. Alle Berechnungen passen sich automatisch an.</p>
    </div>
    <div class="adv-card">
      <div class="icon-badge"><svg viewBox="0 0 24 24"><path d="M14.5 6.5a4 4 0 0 0-5 5L4 17l3 3 5.5-5.5a4 4 0 0 0 5-5l-2.5 2.5-2.5-.5-.5-2.5z"/></svg></div>
      <h3>Montage inklusive</h3>
      <p>Kein Preisvergleich notwendig: Professionelle Installation durch zertifizierte Fachbetriebe ist bereits im Angebot enthalten.</p>
    </div>
  </div>
</section>

<!-- AUDIENCE -->
<section class="section aud">
  <div class="center">
    <span class="pill">Für wen ist der Konfigurator?</span>
    <h2 class="h2">Für wen eignet sich der Konfigurator?</h2>
    <p class="sub">Für alle, die echte Zahlen statt Verkaufsversprechen wollen.</p>
  </div>
  <div class="aud-grid">
    <div class="aud-card">
      <div class="top"><div class="icon-badge"><svg viewBox="0 0 24 24"><path d="M3 11l9-7 9 7M5 10v10h14V10"/><path d="M10 20v-6h4v6"/></svg></div><h3>Privathaushalte</h3></div>
      <p>Neubau oder Bestandsgebäude – egal ob kleines Reihenhausdach oder große Doppelhaushälfte.</p>
    </div>
    <div class="aud-card">
      <div class="top"><div class="icon-badge"><svg viewBox="0 0 24 24"><path d="M3 21V10l6 4V10l6 4V6h6v15z"/></svg></div><h3>Gewerbebetriebe</h3></div>
      <p>Vom Handwerksbetrieb bis zur Industriehalle – wir berechnen jede Anlagengröße.</p>
    </div>
    <div class="aud-card">
      <div class="top"><div class="icon-badge"><svg viewBox="0 0 24 24"><path d="M3 18l3-12h12l3 12z"/><path d="M12 6v12M4.5 12h15"/></svg></div><h3>Kleine Dachflächen</h3></div>
      <p>Auch auf kleinen Flächen lohnt sich Photovoltaik. Unser Konfigurator berechnet das Optimum.</p>
    </div>
    <div class="aud-card">
      <div class="top"><div class="icon-badge"><svg viewBox="0 0 24 24"><rect x="5" y="3" width="14" height="18" rx="2"/><path d="M8 7h8M8 11h2M12 11h2M8 15h2M12 15h2"/></svg></div><h3>Zahlenorientierte</h3></div>
      <p>Für alle, die erst verstehen, dann entscheiden – ohne Verkaufsdruck und ohne Telefonterror.</p>
    </div>
  </div>
  <div class="aud-image" role="img" aria-label="Solarmodule auf einem Aufständerungsgestell"></div>
  <a class="btn">Meine Solaranlage berechnen</a>
</section>

<!-- MODULES -->
<section class="section mod center">
  <span class="pill">Module &amp; Komponenten</span>
  <h2 class="h2">Sie haben die Wahl</h2>
  <p class="sub">Im GLANZHOF Konfigurator wählen Sie Ihre Komponenten selbst aus. Keine Kaufempfehlung mit<br>Verkaufsdruck – nur transparente Optionen.</p>
  <div class="tabs"><span class="tab">Wechselrichter</span><span class="tab active">Solarmodule</span><span class="tab">Energiespeicher</span></div>
  <div class="mod-grid">
    <div class="mod-card">
      <span class="tag">Empfohlen</span>
      <h3>Premium Monokristallin</h3>
      <p class="desc">Hocheffizienz · Schwarz · 25 Jahre Garantie.</p>
      <div class="specs"><div><b>420W</b><span>Leistung</span></div><div><b>22%</b><span>Effizienz</span></div><div><b>A+</b><span>Klasse</span></div></div>
    </div>
    <div class="mod-card">
      <span class="tag">Standard</span>
      <h3>Polykristallin Standard</h3>
      <p class="desc">Kostengünstig · Blau · 20 Jahre Garantie.</p>
      <div class="specs"><div><b>380W</b><span>Leistung</span></div><div><b>19%</b><span>Effizienz</span></div><div><b>A</b><span>Klasse</span></div></div>
    </div>
    <div class="mod-card">
      <span class="tag">Premium+</span>
      <h3>Bifazial HJT Modul</h3>
      <p class="desc">Beidseitig · Maximaler Ertrag · 30 Jahre.</p>
      <div class="specs"><div><b>450W</b><span>Leistung</span></div><div><b>24%</b><span>Effizienz</span></div><div><b>A++</b><span>Klasse</span></div></div>
    </div>
  </div>
  <a class="btn">Module &amp; Speicher selbst auswählen</a>
</section>

<!-- CALCULATION -->
<section class="section calc">
  <div class="calc-card">
    <p class="title">Beispielkalkulation – 10,6 kWp Anlage</p>
    <div class="price"><small>Ab</small><b>18.490</b><small>€</small></div>
    <p class="note">inkl. Montage &amp; MwSt. · Festpreis · keine versteckten Kosten</p>
    <div class="calc-rows">
      <div><span>10,6 kWp Anlage (26 Module)</span><b>13.200 €</b></div>
      <div><span>8,5 kWh Energiespeicher</span><b>4.800 €</b></div>
      <div><span>Montage &amp; Installation</span><b>inkl.</b></div>
      <div><span>Ersparnis/Jahr (Ø)</span><b>+ 1.820 €</b></div>
      <div><span>Amortisation</span><b>ca. 10 Jahre</b></div>
      <div><span>Gewinn nach 20 Jahren</span><b>+ 18.000 €</b></div>
    </div>
    <a class="btn">Meine Anlage berechnen</a>
  </div>
  <div class="calc-right">
    <span class="pill">In wenigen Minuten zu Ihrem Preis</span>
    <h2>Erhalten Sie sofort Ihr Ergebnis</h2>
    <p class="text">Einfach, unverbindlich, anonym und komplett kostenlos. Der GLANZHOF Photovoltaik-Konfigurator ist der erste Preis- und Angebotskonfigurator in Deutschland, bei dem Sie vollständige Ergebnisse ohne persönliche Daten erhalten.</p>
    <ul class="calc-list">
      <li><i class="check"><svg viewBox="0 0 10 10"><path d="M2 5.2l2 2 4-4.4"/></svg></i>Realistischer Angebotspreis</li>
      <li><i class="check"><svg viewBox="0 0 10 10"><path d="M2 5.2l2 2 4-4.4"/></svg></i>Ertrags- &amp; Wirtschaftlichkeitsanalyse</li>
      <li><i class="check"><svg viewBox="0 0 10 10"><path d="M2 5.2l2 2 4-4.4"/></svg></i>Modernes, schlüsselfertiges Solarkonzept</li>
    </ul>
    <a class="btn">PV-Ergebnis jetzt sehen</a>
  </div>
</section>

<!-- REVIEWS -->
<section class="section rev center">
  <span class="pill">Vertrauen &amp; Qualität</span>
  <h2 class="h2">Über 1.000 zufriedene Hausbesitzer</h2>
  <p class="sub">Geprüfte Qualität, zertifizierte Installation und echte Kundenzufriedenheit.</p>
  <div class="rev-grid">
    <div class="rev-card">
      <div class="stars">★★★★★</div>
      <p>Endlich ein Konfigurator ohne Datenfalle! Ich habe meinen Preis sofort gesehen und war begeistert von der Transparenz. Keine nervigen Anrufe danach.</p>
      <div class="who"><span class="avatar">JR</span>Jonas R.</div>
    </div>
    <div class="rev-card">
      <div class="stars">★★★★★</div>
      <p>Super einfach und schnell. In 5 Minuten hatte ich ein vollständiges Angebot inklusive Speicher und Montage. Das Preis-Leistungs-Verhältnis stimmt.</p>
      <div class="who"><span class="avatar">PH</span>Petra H.</div>
    </div>
    <div class="rev-card">
      <div class="stars">★★★★★</div>
      <p>Ich habe mehrere Angebote verglichen. Das GLANZHOF-Angebot war das ehrlichste – keine Überraschungen nach der Montage. Klare Empfehlung!</p>
      <div class="who"><span class="avatar">LB</span>Lukas B.</div>
    </div>
  </div>
</section>

<!-- CTA -->
<section class="section cta center">
  <span class="pill">Jetzt starten</span>
  <h2>Photovoltaik ist eine Investition<br>für Jahrzehnte.</h2>
  <p class="accent">Deshalb sollte sie verstanden werden – nicht verkauft.</p>
  <p class="sub">Starten Sie jetzt Ihren PV-Konfigurator und erhalten Sie in wenigen Minuten Ihr persönliches Ergebnis – kostenlos,<br>anonym und unverbindlich.</p>
  <a class="btn">PV-Konfigurator jetzt starten</a>
</section>

<!-- FOOTER -->
<footer class="section footer">
  <div class="f-brand">
    <div class="brand"><span class="dot"></span>GLANZHOF</div>
    <p>Ihr Photovoltaik-Konfigurator. Ehrlich kalkuliert. Ohne Datenfang. Powered by Wendel LichtWerk.</p>
    <div class="powered"><i></i>Powered by Wendel LichtWerk</div>
  </div>
  <div class="f-col" style="left:496px">
    <h5>KONFIGURATOR</h5>
    <ul><li>PV-Anlage konfigurieren</li><li>So funktioniert's</li><li>Module &amp; Komponenten</li><li>Warum GLANZHOF</li></ul>
  </div>
  <div class="f-col" style="left:704px">
    <h5>INFORMATIONEN</h5>
    <ul><li>FAQ</li><li>Über uns</li><li>Beratung anfragen</li><li>Referenzen</li></ul>
  </div>
  <div class="f-col" style="left:911px">
    <h5>RECHTLICHES</h5>
    <ul><li>Impressum</li><li>Datenschutz</li><li>AGB</li><li>Cookie-Einstellungen</li></ul>
  </div>
  <div class="f-bottom">
    <span>© 2025 GLANZHOF · www.glanzhof-energie.de · Ein Angebot von <b>Wendel LichtWerk</b></span>
    <span>Meta-Keywords: Photovoltaik Konfigurator · Solaranlage berechnen · PV Anlage konfigurieren</span>
  </div>
</footer>

</body>
</html>
```